Lawn care business card

I am looking for a quality designed personal business card to represent the quality and elegant nature of our company. We separate ourselves in our market by the aesthetic value of our work, so I am looking for marketing material that does the same. We target our marketing high end customers, and we try to avoid price shoppers. I am open to all design options, so long as they are in line with our companies values.

We are tend to go with a retro look on everything from our logo and print material, to our uniforms. We like to portray and "old fashion" set of core values, with a modern elegance. So a wild and crazy look is out of the question.

Things I'd like on the card:
1.) Logo
2.) Phone number: (816) 555-0193
3.) Website: Verdanthollow.com
4.) Email: peterwalsh@verdanthollow.com
5.) My name: Peter Walsh
6.) Facebook link: facebook.com/GreenridgeLawnandLandscape
7.) Instagram: http://instagram.com/verdanthollow

Attached is a copy of our logo.

```html
<!DOCTYPE html>
<html lang="en">
<head>
<meta charset="utf-8">
<title>Verdant Hollow – Business Card</title>
<link href="https://fonts.googleapis.com/css2?family=Arimo:wght@400;700&display=swap" rel="stylesheet">
<style>
  :root {
    --backdrop: #e4e4e2;
    --card-white: #ffffff;
    --brand-orange: #e23f15;
    --ink: #1f1f1f;
    --icon-dark: #1a1a1a;
  }
  html, body {
    margin: 0;
    padding: 0;
    width: 1200px;
    height: 960px;
    overflow: hidden;
    background: var(--backdrop);
    font-family: "Arimo", Arial, sans-serif;
  }
  .business-card {
    position: absolute;
    left: 75px;
    top: 180px;
    width: 1050px;
    height: 600px;
    background: var(--card-white);
    overflow: hidden;
  }
  .brand-band {
    position: absolute;
    left: 0;
    top: 0;
    width: 1050px;
    height: 600px;
  }
  .brand-mark {
    position: absolute;
    left: 155px;
    top: 160px;
    width: 320px;
    display: flex;
    align-items: center;
    justify-content: center;
    gap: 10px;
  }
  .brand-dot {
    width: 16px;
    height: 16px;
    border-radius: 50%;
    background: var(--brand-orange);
    flex: none;
  }
  .brand-name {
    font-size: 30px;
    font-weight: 700;
    letter-spacing: 1px;
    color: var(--ink);
    text-transform: uppercase;
  }
  .holder-name {
    position: absolute;
    right: 70px;
    top: 140px;
    margin: 0;
    font-size: 46px;
    font-weight: 400;
    color: var(--brand-orange);
  }
  .contact-list {
    position: absolute;
    left: 272px;
    top: 348px;
    margin: 0;
    padding: 0;
    list-style: none;
  }
  .contact-item {
    display: flex;
    align-items: center;
    height: 45px;
    font-size: 25px;
    color: var(--ink);
  }
  .contact-icon {
    width: 26px;
    height: 26px;
    margin-right: 42px;
    flex: none;
  }
</style>
</head>
<body>
  <section class="business-card">
    <svg class="brand-band" viewBox="0 0 1050 600" aria-hidden="true">
      <rect x="0" y="0" width="210" height="600" fill="var(--brand-orange)"/>
      <circle cx="315" cy="180" r="165" fill="var(--card-white)"/>
    </svg>

    <div class="brand-mark">
      <span class="brand-dot"></span>
      <span class="brand-name">Verdant Hollow</span>
    </div>

    <h1 class="holder-name">Peter Walsh</h1>

    <ul class="contact-list">
      <li class="contact-item">
        <svg class="contact-icon" viewBox="0 0 26 26" aria-hidden="true">
          <rect width="26" height="26" rx="3" fill="var(--icon-dark)"/>
          <path d="M8 7c1-1 2 0 2.5 1.5l.5 1.5-1.5 1.2c.8 1.8 2 3 3.8 3.8l1.2-1.5 1.5.5c1.5.5 2.5 1.5 1.5 2.5-1 1.3-2.5 1.8-4.5 1-3-1.3-5.5-3.8-6.8-6.8-.8-2-.3-3.5 1.8-3.7z" fill="#fff"/>
        </svg>
        (816) 555-0193
      </li>
      <li class="contact-item">
        <svg class="contact-icon" viewBox="0 0 26 26" aria-hidden="true">
          <rect width="26" height="26" rx="3" fill="var(--icon-dark)"/>
          <circle cx="13" cy="13" r="7" fill="none" stroke="#fff" stroke-width="1.6"/>
          <ellipse cx="13" cy="13" rx="3" ry="7" fill="none" stroke="#fff" stroke-width="1.3"/>
          <line x1="6" y1="13" x2="20" y2="13" stroke="#fff" stroke-width="1.3"/>
        </svg>
        Verdanthollow.com
      </li>
      <li class="contact-item">
        <svg class="contact-icon" viewBox="0 0 26 26" aria-hidden="true">
          <rect width="26" height="26" rx="3" fill="var(--icon-dark)"/>
          <rect x="6" y="8" width="14" height="10" fill="none" stroke="#fff" stroke-width="1.5"/>
          <path d="M6 8l7 6 7-6" fill="none" stroke="#fff" stroke-width="1.5"/>
        </svg>
        peterwalsh@verdanthollow.com
      </li>
      <li class="contact-item">
        <svg class="contact-icon" viewBox="0 0 26 26" aria-hidden="true">
          <rect width="26" height="26" rx="3" fill="var(--icon-dark)"/>
        </svg>
        http://instagram.com/verdanthollow
      </li>
      <li class="contact-item">
        <svg class="contact-icon" viewBox="0 0 26 26" aria-hidden="true">
          <rect width="26" height="26" rx="3" fill="var(--icon-dark)"/>
        </svg>
        facebook.com/GreenridgeLawnandLandscape
      </li>
    </ul>
  </section>
</body>
</html>
```